Mobile Oil Change company needs a flyer to promote new business

We need a flyer to 1) print & handout and 2) email out to potential customers. We are a mobile oil change company that comes to our customer locations to perform the work instead of customers going to traditional oil change companies. We have a 21 point inspection with our oil change. (21 point inspection details will not be on the flyer). Would like to keep the flyer simple but creative. I'm attaching 1) the write-up we created, 2) our logo (logo color is dark teal on white but other combinations are included if you wanted to propose a different color combination), and 3) additional services we offer. Logo font is Alegreya Sans.
Would like the additional services listed with icons and brief descriptions (similar to attachment) without pricing. Company website for reference is www.brindlefleetcare.com.

Target Market(s)

Companies with many service vehicles such as Oil & Gas service companies, heating and air conditioning companies, utility companies, police departments, etc. Companies that prioritize convenience and maintenance first.

Font styles to use
Sans Serif

Colors
00a990

Requirements
Must have
• Simple but creative design with our logo at top of the flyer. Additional Services (details in document supplied) can be smaller and less prominent than other "main" content listed in the CONTENT document supplied.
Should not have
• Do not use animated character graphics in the flyer and limit (1) stock photos to A small area in the flyer.

```html
<!DOCTYPE html>
<html lang="en">
<head>
<meta charset="utf-8">
<title>Brindle Fleet Care – Mobile Oil Change Flyer</title>
<link rel="stylesheet" href="https://fonts.googleapis.com/css2?family=Arimo:wght@700&family=Lato:wght@400;700;900&family=Roboto+Condensed:wght@400;700&display=swap">
<style>
  :root {
    --teal: #17a78f;
    --teal-deep: #1c5a5b;
    --slate: #2f5253;
    --slate-text: #24464c;
    --gold: #f2c12e;
    --white: #ffffff;
    --paper: #ffffff;
  }
  * { box-sizing: border-box; margin: 0; padding: 0; }
  html, body { width: 1023px; height: 1200px; overflow: hidden; background: var(--paper); }
  .flyer { position: relative; width: 1023px; height: 1200px; background: var(--white); font-family: "Lato", sans-serif; overflow: hidden; }

  .headline-band { position: absolute; left: 0; top: 0; width: 1023px; height: 468px; background: var(--teal); }
  .headline { position: absolute; left: 0; top: 30px; width: 1023px; text-align: center; font-family: "Arimo", sans-serif; font-weight: 700; font-size: 39px; color: var(--white); letter-spacing: 0.3px; }

  .hero-frame { position: absolute; left: 0; top: 100px; width: 1008px; height: 368px; background: var(--white); border-radius: 0 66px 0 0; }
  .hero-photo { position: absolute; left: 0; top: 108px; width: 1000px; height: 360px; border-radius: 0 60px 0 0; background: linear-gradient(120deg, #3b4650 0%, #4f5c68 40%, #36414b 70%, #2a333c 100%); }
  .hero-shade { position: absolute; left: 0; top: 108px; width: 620px; height: 300px; background: linear-gradient(90deg, rgba(20,28,36,.55), rgba(20,28,36,0)); }

  .perks { position: absolute; left: 26px; top: 188px; list-style: none; color: var(--white); font-size: 19px; line-height: 1.25; }
  .perks li { position: relative; padding-left: 33px; margin-bottom: 14px; max-width: 400px; }
  .perks svg { position: absolute; left: 0; top: -3px; }

  .content-panel { position: absolute; left: 0; top: 468px; width: 1023px; height: 263px; background: var(--white); }
  .logo-tab { position: absolute; left: 0; top: 418px; width: 445px; height: 60px; background: var(--white); border-radius: 0 40px 0 0; }

  .engine-art { position: absolute; left: 540px; top: 296px; width: 450px; height: 232px; border-radius: 50% 45% 40% 50%; background: radial-gradient(ellipse at 45% 55%, #8d9499 0%, #c8b04a 45%, rgba(240,196,40,.5) 70%, rgba(240,196,40,0) 100%); }

  .brand { position: absolute; left: 30px; top: 500px; display: flex; align-items: center; gap: 14px; }
  .brand-dot { width: 22px; height: 22px; border-radius: 50%; background: var(--teal); }
  .brand-name { font-family: "Lato", sans-serif; font-weight: 900; font-size: 44px; color: var(--teal); letter-spacing: 0.5px; }

  .intro { position: absolute; left: 22px; top: 612px; width: 425px; font-size: 20.5px; line-height: 1.4; color: var(--slate-text); }

  .steps { position: absolute; left: 508px; top: 556px; list-style: none; font-size: 17.5px; line-height: 22px; color: var(--slate-text); }
  .steps li { position: relative; padding-left: 27px; margin-bottom: 8px; max-width: 450px; }
  .steps svg { position: absolute; left: 0; top: 3px; }

  .services-rule { position: absolute; left: 0; top: 731px; width: 1023px; height: 14px; background: var(--teal); }
  .services-band { position: absolute; left: 0; top: 745px; width: 1023px; height: 362px; background: linear-gradient(180deg, #35585a 0%, #2c4c4e 60%, #33595b 100%); }
  .services-tab { position: absolute; left: 290px; top: 728px; width: 445px; height: 70px; background: var(--teal); border-radius: 0 0 36px 36px; text-align: center; font-family: "Roboto Condensed", sans-serif; font-weight: 700; font-size: 36px; line-height: 70px; color: var(--white); }

  .service { position: absolute; width: 430px; height: 80px; }
  .service-icon { position: absolute; left: 0; top: 0; width: 74px; height: 74px; border-radius: 50%; border: 2.5px solid var(--white); display: flex; align-items: center; justify-content: center; }
  .service-icon::before { content: ""; position: absolute; inset: 5px; border-radius: 50%; border: 1.5px solid rgba(23,167,143,.8); }
  .service-text { position: absolute; left: 104px; top: 0; width: 322px; }
  .service-title { font-family: "Roboto Condensed", sans-serif; font-weight: 700; font-size: 19.5px; color: var(--gold); line-height: 1; margin-bottom: 2px; }
  .service-desc { font-size: 15px; line-height: 1.08; color: var(--white); text-align: justify; }

  .footer-gap { position: absolute; left: 0; top: 1107px; width: 1023px; height: 24px; background: var(--white); }
  .footer { position: absolute; left: 0; top: 1131px; width: 1023px; height: 69px; background: var(--teal-deep); display: flex; align-items: center; justify-content: space-between; padding: 0 28px 0 40px; font-family: "Roboto Condensed", sans-serif; font-size: 24px; color: var(--white); }
  .contact { display: flex; align-items: center; gap: 9px; }
</style>
</head>
<body>
<main class="flyer">
  <div class="headline-band"></div>
  <h1 class="headline">HASSLE FREE OIL CHANGES ON YOUR TERMS</h1>

  <div class="hero-frame"></div>
  <div class="hero-photo" role="img" aria-label="Photo of a technician in work gloves servicing a vehicle engine under an open hood"></div>
  <div class="hero-shade"></div>

  <ul class="perks">
    <li><svg width="22" height="22" viewBox="0 0 22 22"><rect x="2" y="4" width="15" height="15" rx="2" fill="none" stroke="#f2c12e" stroke-width="2"/><path d="M6 11l4 4 10-12" fill="none" stroke="#f2c12e" stroke-width="2.4"/></svg>Service includes a 21-point inspection</li>
    <li><svg width="22" height="22" viewBox="0 0 22 22"><rect x="2" y="4" width="15" height="15" rx="2" fill="none" stroke="#f2c12e" stroke-width="2"/><path d="M6 11l4 4 10-12" fill="none" stroke="#f2c12e" stroke-width="2.4"/></svg>Additional services are available</li>
    <li><svg width="22" height="22" viewBox="0 0 22 22"><rect x="2" y="4" width="15" height="15" rx="2" fill="none" stroke="#f2c12e" stroke-width="2"/><path d="M6 11l4 4 10-12" fill="none" stroke="#f2c12e" stroke-width="2.4"/></svg>High quality synthetic oil used is best suited for commercial vehicles</li>
  </ul>

  <div class="content-panel"></div>
  <div class="logo-tab"></div>
  <div class="engine-art" role="img" aria-label="Illustration of a car engine wrapped in a golden motor oil splash"></div>

  <div class="brand"><span class="brand-dot"></span><span class="brand-name">Brindle Fleet Care</span></div>

  <p class="intro">Our simple 5-step process lets you schedule an appointment and get service to save time and money:</p>

  <ul class="steps">
    <li><svg width="16" height="16" viewBox="0 0 16 16"><circle cx="8" cy="8" r="6.8" fill="none" stroke="#17a78f" stroke-width="1.5"/><path d="M6.5 4.8L9.7 8l-3.2 3.2" fill="none" stroke="#17a78f" stroke-width="1.8"/></svg>Call or email us to schedule service</li>
    <li><svg width="16" height="16" viewBox="0 0 16 16"><circle cx="8" cy="8" r="6.8" fill="none" stroke="#17a78f" stroke-width="1.5"/><path d="M6.5 4.8L9.7 8l-3.2 3.2" fill="none" stroke="#17a78f" stroke-width="1.8"/></svg>Our highly trained technicians come to you for service</li>
    <li><svg width="16" height="16" viewBox="0 0 16 16"><circle cx="8" cy="8" r="6.8" fill="none" stroke="#17a78f" stroke-width="1.5"/><path d="M6.5 4.8L9.7 8l-3.2 3.2" fill="none" stroke="#17a78f" stroke-width="1.8"/></svg>Service is performed quickly on your vehicle</li>
    <li><svg width="16" height="16" viewBox="0 0 16 16"><circle cx="8" cy="8" r="6.8" fill="none" stroke="#17a78f" stroke-width="1.5"/><path d="M6.5 4.8L9.7 8l-3.2 3.2" fill="none" stroke="#17a78f" stroke-width="1.8"/></svg>Pay agreed-upon pricing and receipt is emailed to you</li>
    <li><svg width="16" height="16" viewBox="0 0 16 16"><circle cx="8" cy="8" r="6.8" fill="none" stroke="#17a78f" stroke-width="1.5"/><path d="M6.5 4.8L9.7 8l-3.2 3.2" fill="none" stroke="#17a78f" stroke-width="1.8"/></svg>Services performed are tracked electronically and<br>reminders created</li>
  </ul>

  <div class="services-rule"></div>
  <div class="services-band" role="img" aria-label="Dimmed photo of an engine bay behind the services list"></div>
  <h2 class="services-tab">OUR SERVICES</h2>

  <section class="service" style="left:40px; top:820px;">
    <div class="service-icon"><svg width="40" height="40" viewBox="0 0 40 40" fill="none" stroke="#17a78f" stroke-width="2"><rect x="6" y="6" width="28" height="28" rx="2"/><path d="M15 6v28M25 6v28M6 13h28M6 20h28M6 27h28"/></svg></div>
    <div class="service-text"><h3 class="service-title">ENGINE AIR FILTER REPLACEMENT</h3><p class="service-desc">Maintain optimum engine performace. Recomended every 15,000 to 30,000 miles.</p></div>
  </section>
  <section class="service" style="left:40px; top:913px;">
    <div class="service-icon"><svg width="40" height="40" viewBox="0 0 40 40" fill="none" stroke="#17a78f" stroke-width="2"><rect x="9" y="5" width="22" height="30" rx="2"/><path d="M13 13c3-2 6 2 9 0s5 0 5 0M13 19c3-2 6 2 9 0s5 0 5 0M13 25c3-2 6 2 9 0s5 0 5 0"/></svg></div>
    <div class="service-text"><h3 class="service-title">CABIN AIR FILTER REPLACEMENT</h3><p class="service-desc">Maintain a clean A/C and fan system. Recomended every 15,000 to 25,000 miles or 12 months.</p></div>
  </section>
  <section class="service" style="left:40px; top:1003px;">
    <div class="service-icon"><svg width="40" height="40" viewBox="0 0 40 40" fill="none" stroke="#17a78f" stroke-width="2"><path d="M5 14c10-6 20-6 30 0l-4 16H9z"/><path d="M20 32l-8-14"/></svg></div>
    <div class="service-text"><h3 class="service-title">WIPERBLADE REPLACEMENT</h3><p class="service-desc">Maintain excellent visability on the road. Recommended every 6 to 12 month.</p></div>
  </section>

  <section class="service" style="left:540px; top:820px;">
    <div class="service-icon"><svg width="40" height="40" viewBox="0 0 40 40" fill="none" stroke="#17a78f" stroke-width="2"><circle cx="20" cy="20" r="14"/><circle cx="20" cy="20" r="4"/><path d="M6 18h10M24 18h10M20 24v10"/></svg></div>
    <div class="service-text"><h3 class="service-title">POWER STEERING FLUID FLUSH</h3><p class="service-desc">Maintain proper power steering systetm health. Recomended every 30,000 to 60,000 miles</p></div>
  </section>
  <section class="service" style="left:540px; top:913px;">
    <div class="service-icon"><svg width="40" height="40" viewBox="0 0 40 40" fill="none" stroke="#17a78f" stroke-width="2"><rect x="9" y="7" width="16" height="27" rx="2"/><rect x="12" y="11" width="10" height="7"/><path d="M25 15l5 4v11a2 2 0 0 0 4 0V17l-4-5"/></svg></div>
    <div class="service-text"><h3 class="service-title">FUEL SYSTEM TREATMENT</h3><p class="service-desc">Clean your fuel system and injectors to improve fuel economy.</p></div>
  </section>
  <section class="service" style="left:540px; top:1003px;">
    <div class="service-icon"><svg width="40" height="40" viewBox="0 0 40 40" fill="none" stroke="#17a78f" stroke-width="2"><circle cx="18" cy="22" r="12"/><circle cx="18" cy="22" r="4"/><path d="M24 8a14 14 0 0 1 10 10l-6 2"/></svg></div>
    <div class="service-text"><h3 class="service-title">BRAKE FLUID FLUSH</h3><p class="service-desc">Maintain an excelent functioning brake system. Recomended every 20,000 miles or 2 years.</p></div>
  </section>

  <div class="footer-gap"></div>
  <footer class="footer">
    <span class="contact"><svg width="22" height="22" viewBox="0 0 22 22"><circle cx="11" cy="11" r="10" fill="none" stroke="#fff" stroke-width="1.6"/><rect x="5.5" y="7" width="11" height="8" fill="#fff"/><path d="M5.5 7l5.5 4.5L16.5 7" fill="none" stroke="#1c5a5b" stroke-width="1.3"/></svg>Sales@BrindleFleetCare.com</span>
    <span class="contact"><svg width="22" height="22" viewBox="0 0 22 22"><circle cx="11" cy="11" r="10" fill="none" stroke="#fff" stroke-width="1.6"/><path d="M7 6c-1 2 0 5 3 8s6 4 7 3l-2-3-2 1c-1-1-2-2-3-4l1-2z" fill="#fff"/></svg>(833) 555-0148</span>
    <span class="contact"><svg width="22" height="22" viewBox="0 0 22 22" fill="none" stroke="#fff" stroke-width="1.4"><circle cx="11" cy="11" r="10"/><circle cx="11" cy="11" r="6"/><ellipse cx="11" cy="11" rx="2.6" ry="6"/><path d="M5 11h12"/></svg>BrindleFleetCare.com</span>
  </footer>
</main>
</body>
</html>
```